CBD Oil manufacturer needs a label/logo.

We need a label/logo design for our CBD oil bottles. The brand name is Velora - meaning immortality. CBD oil is made from the hemp plant, usually used medicinally. We are open to color schemes and designs. I am attaching a label that someone else made - but we do not like at all. The information listed on the side does need to be included.

Target Market(s)

CBD Oil Retailers - generally for medicinal purposes. Geared towards all ages, etc.

Industry/Entity Type

Manufacturer

Requirements
Must have
• Supplement Facts, Suggested use, Other Ingredients, Manufactured by, etc. AS SEEN ON ATTACHMENT.

```html
<!DOCTYPE html>
<html lang="en">
<head>
<meta charset="utf-8">
<title>Velora Hemp Tincture Labels</title>
<link href="https://fonts.googleapis.com/css2?family=Cinzel:wght@400;500&family=Arimo:wght@400;700&display=swap" rel="stylesheet">
<style>
  :root {
    --backdrop: #e6e7e8;
    --paper: #ffffff;
    --brand-green: #0f6b35;
    --sun-yellow: #f6cf1e;
    --cocoa: #4a2219;
    --ink: #231f20;
    --shadow: rgba(0,0,0,0.55);
  }
  * { margin: 0; padding: 0; box-sizing: border-box; }
  html, body { width: 1200px; height: 960px; overflow: hidden; background: var(--backdrop); }
  .sheet { position: relative; width: 1200px; height: 960px; }
  .label {
    position: absolute; left: 96px; width: 1008px; height: 368px;
    box-shadow: 12px 12px 10px var(--shadow);
  }
  .label--light { top: 78px; }
  .label--dark { top: 524px; }
  .label svg { display: block; width: 100%; height: 100%; }
  .brand-name { font-family: "Cinzel", serif; font-weight: 400; letter-spacing: 4px; }
  .serif-caps { font-family: "Cinzel", serif; letter-spacing: 3px; }
  .sans { font-family: "Arimo", Arial, sans-serif; }
  .bold { font-weight: 700; }
</style>
</head>
<body>
<main class="sheet">

  <!-- Light version -->
  <section class="label label--light">
    <svg viewBox="0 0 840 307" xmlns="http://www.w3.org/2000/svg">
      <rect class="label-paper" width="840" height="307" fill="var(--paper)"/>
      <path class="wave-band" d="M0,280 C150,250 300,228 420,246 C520,262 620,300 700,295 C770,290 820,276 840,270 L840,307 L0,307 Z" fill="var(--brand-green)"/>
      <path class="wave-stripe" d="M0,272 C150,242 300,220 420,238 C520,254 620,292 700,287 C770,282 820,268 840,262" fill="none" stroke="var(--sun-yellow)" stroke-width="4"/>

      <circle class="brand-dot" cx="280" cy="40" r="9" fill="var(--brand-green)"/>
      <text class="brand-name" x="280" y="150" text-anchor="middle" font-size="62" fill="var(--cocoa)">VELORA</text>
      <text class="sans" x="280" y="180" text-anchor="middle" font-size="20" fill="var(--brand-green)">1,000 mg Cannabidol</text>
      <line x1="50" y1="197" x2="470" y2="197" stroke="var(--cocoa)" stroke-width="1.3"/>
      <text class="sans bold" x="250" y="222" text-anchor="middle" font-size="16" fill="var(--brand-green)">HEMP</text>
      <text class="serif-caps" x="210" y="282" font-size="11" fill="var(--paper)">TINCTURE</text>

      <text class="sans" transform="translate(544,240) rotate(-90)" font-size="13" fill="var(--brand-green)">whole hemp and coconut oils</text>

      <g class="info-panel sans" fill="var(--ink)">
        <text class="bold" x="613" y="30" font-size="11.5">Suggested Use: 1/2 dropper</text>
        <text class="bold" x="613" y="43" font-size="11.5">per 100 lbs. as needed.</text>
        <rect x="613" y="57" width="105" height="104" fill="var(--sun-yellow)"/>
        <text class="bold" x="619" y="69" font-size="9">Supplement Facts</text>
        <g font-size="7.4" class="bold">
          <text x="613" y="177">Other Ingredients:</text>
          <text x="613" y="186">Coconut Oil (MCT), Raw</text>
          <text x="613" y="195">Coconut Oil.</text>
          <text x="613" y="211">Manufactured by:</text>
          <text x="613" y="220">Northfield Botanics, LLC</text>
          <text x="613" y="229">Ridgeview, CO, 80000</text>
          <text x="613" y="238">555 - 010 - 4821</text>
          <text x="732" y="69">Shake well before using.</text>
          <text x="732" y="78">Store in a cool, dry place,</text>
          <text x="732" y="87">away from light.</text>
          <text x="732" y="108">Not to be used during</text>
          <text x="732" y="117">pregnancy or lactation.</text>
          <text x="732" y="126">If you have a medical</text>
          <text x="732" y="135">condition or take</text>
          <text x="732" y="144">pharmaceutical drugs,</text>
          <text x="732" y="153">please consult your</text>
          <text x="732" y="162">physician before use.</text>
          <text x="732" y="171">Keep out of reach of</text>
          <text x="732" y="180">children.</text>
          <text x="732" y="200">Do not use if safety seal</text>
          <text x="732" y="209">is broken or missing.</text>
          <text x="732" y="225">BATCH#: 031616</text>
          <text x="692" y="262" text-anchor="middle">For more information please visit:</text>
          <text x="692" y="271" text-anchor="middle">www.northfieldbotanics.com</text>
        </g>
      </g>
    </svg>
  </section>

  <!-- Dark version -->
  <section class="label label--dark">
    <svg viewBox="0 0 840 307" xmlns="http://www.w3.org/2000/svg">
      <rect width="840" height="307" fill="var(--brand-green)"/>
      <path class="wave-paper" d="M0,280 C150,250 300,228 420,246 C520,262 620,300 700,295 C770,290 820,276 840,270 L840,307 L0,307 Z" fill="var(--paper)"/>
      <path d="M0,283 C150,253 300,231 420,249 C520,265 620,303 700,298 C770,293 820,279 840,273" fill="none" stroke="var(--brand-green)" stroke-width="3"/>
      <path class="wave-stripe" d="M0,272 C150,242 300,220 420,238 C520,254 620,292 700,287 C770,282 820,268 840,262" fill="none" stroke="var(--sun-yellow)" stroke-width="4"/>

      <circle class="brand-dot" cx="280" cy="40" r="9" fill="var(--sun-yellow)"/>
      <text class="brand-name" x="280" y="150" text-anchor="middle" font-size="62" fill="var(--sun-yellow)">VELORA</text>
      <text class="sans" x="280" y="180" text-anchor="middle" font-size="20" fill="var(--paper)">1,000 mg Cannabidol</text>
      <line x1="50" y1="197" x2="470" y2="197" stroke="var(--sun-yellow)" stroke-width="1.3"/>
      <text class="sans bold" x="250" y="222" text-anchor="middle" font-size="16" fill="var(--paper)">HEMP</text>
      <text class="serif-caps" x="154" y="282" font-size="11" fill="var(--brand-green)">TINCTURE</text>

      <text class="sans" transform="translate(544,240) rotate(-90)" font-size="13" fill="var(--paper)">whole hemp and coconut oils</text>

      <g class="info-panel sans" fill="var(--paper)">
        <text class="bold" x="613" y="30" font-size="11.5">Suggested Use: 1/2 dropper</text>
        <text class="bold" x="613" y="43" font-size="11.5">per 100 lbs. as needed.</text>
        <rect x="613" y="57" width="105" height="104" fill="var(--paper)"/>
        <text class="bold" x="619" y="69" font-size="9" fill="var(--ink)">Supplement Facts</text>
        <g font-size="7.4" class="bold">
          <text x="613" y="177">Other Ingredients:</text>
          <text x="613" y="186">Coconut Oil (MCT), Raw</text>
          <text x="613" y="195">Coconut Oil.</text>
          <text x="613" y="211">Manufactured by:</text>
          <text x="613" y="220">Northfield Botanics, LLC</text>
          <text x="613" y="229">Ridgeview, CO, 80000</text>
          <text x="613" y="238">555 - 010 - 4821</text>
          <text x="732" y="69">Shake well before using.</text>
          <text x="732" y="78">Store in a cool, dry place,</text>
          <text x="732" y="87">away from light.</text>
          <text x="732" y="108">Not to be used during</text>
          <text x="732" y="117">pregnancy or lactation.</text>
          <text x="732" y="126">If you have a medical</text>
          <text x="732" y="135">condition or take</text>
          <text x="732" y="144">pharmaceutical drugs,</text>
          <text x="732" y="153">please consult your</text>
          <text x="732" y="162">physician before use.</text>
          <text x="732" y="171">Keep out of reach of</text>
          <text x="732" y="180">children.</text>
          <text x="732" y="200">Do not use if safety seal</text>
          <text x="732" y="209">is broken or missing.</text>
          <text x="732" y="225">BATCH#: 031616</text>
        </g>
        <g font-size="7.4" class="bold" fill="var(--brand-green)">
          <text x="692" y="262" text-anchor="middle" fill="var(--paper)">For more information please visit:</text>
          <text x="692" y="271" text-anchor="middle" fill="var(--paper)">www.northfieldbotanics.com</text>
        </g>
      </g>
    </svg>
  </section>

</main>
</body>
</html>
```